Brochure Design Project

Check our www.harbourlanehomes.example. Company Name is "Harbour Lane Living" and the brochure is to be named "Golden Tides Ahead".

We are seeking a brochure that captures the essence of the idea of living aboard a cruise ship in retirement therefore must encompass not only cruising but also retirement living, therefore we're promoting "a lifestyle better than living ashore in a retirement village".

Brochure will be around 20+ pages though there will only most likely only be around 6 pages of actual templates needed which can be used interchangeably plus a front and back cover.

Some pictures on the brochure will take up full pages with maybe a caption so these other pages should be pretty quick.

Must have great presence and "feel" about it.

Friendly, cheery brochure with bright colours.

Must "look a million dollars" as the market we're targeting is very selective and we're competing in a very competitive market, retirement villages where our clientele is investing large sums of money in their retirement and they are basing their decision on whether to trust us on possibly only this brochure.

This is a new project that will launch on television, radio, pamphlet and brochure in the next 6 weeks.

Work on a brochure I'd been doing attached. Don't just want a repeat of this brochure. This is to provide you with various pieces of text to start the brochure, not to copy the design, which I think is antique and needs completely redoing.

Project Deadline Extended
Reason: At present we have only received a few designs and at present none of them are truly suitable to what we're after or require quite a few changes in terms of creativity to even come close to what we'd be expecting from professional graphic designers.

Project Deadline Extended
Reason: New designers have accepted the invitation to submit designs and many have only had a couple of days to submit designs.

If you haven't already submitted your final designs, please finalise and submit them. Deadline is almost reached.

We look forward to the seeing the final submissions.

Regards,

Harbour Lane Living Ltd.

50+ age bracket (therefore larger writing for brochure text)

Radio

Must have
• We are after classy and sophisticated, not gaudy and cheap so the design must look formal yet modern and eschew the virtues of contemporary and exotic and a higher standard of retirement living rather than "bright, gaudy, cheap and a quick buck".

Our company is designed to provide sophisticated and practical living arrangements for people that are looking for comfortable, practical yet stylishly different in terms of the elegance and lifestyle that people would normally expect for the price of standard living arrangements.

Brochure when completed must be sent in an editable format rather than just static.

Must have a section for pricing comparison between costs of living in "Own Home vs. Retirement Village vs. Harbour Lane Living" for comparision of costs.

Must also have a second comparison with the same titles though this is a "Features/Facilities Comparison".

Must use only royalty-free photography.

Must NOT use pictures of GIANT cruise ships. The ships we're providing our clientelle are mid-1990's ships therefore have a capacity of around 800-1000 capacity, not like today's MEGA-liners that hold 2000-5000 passengers. We don't want to mislead our clientele.

Must NOT use pictures of ships with any names or logos on them (to forestall the possibility of copyright and trademark infringement).

```html
<!DOCTYPE html>
<html lang="en">
<head>
<meta charset="utf-8">
<title>Golden Tides Ahead – Benefits Spread</title>
<link rel="stylesheet" href="https://fonts.googleapis.com/css2?family=Source+Sans+3:wght@300;400;600&family=Dancing+Script:wght@500&display=swap">
<style>
  :root {
    --backdrop: #1d1d1e;
    --page: #ffffff;
    --magenta: #b3226f;
    --magenta-bright: #e3287c;
    --magenta-deep: #9c1a5e;
    --body-grey: #707070;
    --list-grey: #4e4e4e;
    --sky: #7fbbe6;
    --fold: #bdbdbd;
    --folio: #5a5a5a;
  }
  * { box-sizing: border-box; margin: 0; padding: 0; }
  html, body { width: 1200px; height: 1000px; overflow: hidden; }
  body {
    position: relative;
    background: var(--backdrop);
    font-family: "Source Sans 3", "Helvetica Neue", Arial, sans-serif;
  }
  .spread { position: absolute; left: 65px; top: 72px; width: 1071px; height: 758px; }

  .photo-couple {
    position: absolute; left: 0; top: 0; width: 535px; height: 758px;
    background:
      radial-gradient(ellipse at 30% 20%, #e9e3a8 0%, rgba(233,227,168,0) 45%),
      radial-gradient(ellipse at 75% 35%, #c8683e 0%, rgba(200,104,62,0) 40%),
      radial-gradient(ellipse at 35% 65%, #c45a55 0%, rgba(196,90,85,0) 40%),
      radial-gradient(ellipse at 50% 95%, #f1eeea 0%, rgba(241,238,234,0) 45%),
      linear-gradient(180deg, #a9ad6a 0%, #7e8c4a 45%, #8f6e4e 75%, #d9d2c8 100%);
  }
  .photo-couple-veil {
    position: absolute; left: 127px; top: 625px; width: 408px; height: 68px;
    background: linear-gradient(90deg, rgba(179,34,111,0) 0%, rgba(179,34,111,0.55) 55%, rgba(156,26,94,0.85) 100%);
  }

  .page-right { position: absolute; left: 535px; top: 0; width: 536px; height: 758px; background: var(--page); }
  .headline {
    position: absolute; left: 32px; top: 30px; width: 475px;
    font-weight: 300; font-size: 21px; line-height: 26px; color: var(--magenta);
    text-align: justify; text-align-last: left;
  }
  .intro {
    position: absolute; left: 32px; top: 100px; width: 152px;
    font-size: 8.4px; line-height: 12.4px; color: var(--body-grey); text-align: justify;
  }
  .intro p + p { margin-top: 12.4px; }
  .benefits { position: absolute; left: 193px; top: 100px; width: 315px; }
  .benefits-lead { font-size: 8.4px; color: var(--body-grey); margin-bottom: 6px; }
  .benefit-list { list-style: none; }
  .benefit-list li {
    position: relative; padding-left: 12px;
    font-size: 8.4px; line-height: 19.8px; color: var(--list-grey);
  }
  .benefit-list li::before { content: "•"; position: absolute; left: 0; color: var(--body-grey); }

  .benefits-band {
    position: absolute; left: 0; top: 483px; width: 536px; height: 142px;
    background: linear-gradient(90deg, var(--magenta-bright) 0%, #c71f70 55%, var(--magenta-deep) 100%);
    color: #fff;
  }
  .band-title {
    position: absolute; right: 30px; top: 20px;
    font-family: "Dancing Script", cursive; font-weight: 500; font-size: 40px; line-height: 48px;
  }
  .band-tagline {
    position: absolute; right: 30px; top: 79px; text-align: right;
    font-size: 10.5px; line-height: 20px; letter-spacing: 0.9px; text-transform: uppercase;
  }
  .band-tagline span { display: block; }
  .band-tagline span:first-child { margin-right: 85px; }

  .accent-sky { position: absolute; left: 0; top: 625px; width: 32px; height: 68px; background: var(--sky); }
  .photo-deck {
    position: absolute; left: 192px; top: 625px; width: 344px; height: 133px;
    background:
      linear-gradient(180deg, #e9eef2 0%, #bfd0dc 30%, #8a6a4a 42%, #6c3f24 60%, #c98d55 80%, #b57a45 100%);
  }

  .fold { position: absolute; left: 599px; top: 38px; width: 1px; height: 824px; background: var(--fold); }
  .folio { position: absolute; top: 862px; font-size: 17px; font-weight: 300; color: var(--folio); }
  .folio-left { left: 65px; }
  .folio-right { right: 64px; }
</style>
</head>
<body>
  <div class="spread">
    <div class="photo-couple" role="img" aria-label="Photograph: a smiling retired couple sharing lunch at a garden table surrounded by palms and flowers"></div>
    <div class="photo-couple-veil"></div>

    <section class="page-right">
      <h1 class="headline">So what are the benefits of coming on-board as a resident/stateroom owner? That’s easy to answer!</h1>

      <div class="intro">
        <p>Lorem ipsum dolor sit amet, consectetur adipiscing elit. Nunc adipiscing dolor ut sem tincidunt in imperdiet tortor dignissim. Vestibulum ante ipsum primis in faucibus orci luctus et ultrices posuere cubilia Curae; Nunc ac massa massa. In et risus leo, commodo laoreet risus.</p>
        <p>Suspendisse facilisis porttitor tellus, sed eleifend tellus semper vitae. Etiam rhoncus, magna vel tincidunt tincidunt, erat augue volutpat nisi, ac volutpat est arcu a lectus.</p>
        <p>Pellentesque cursus mattis eros vel lobortis. Etiam in purus odio, in malesuada mauris. Mauris mattis magna eget magna volutpat eu pulvinar metus tristique.</p>
      </div>

      <div class="benefits">
        <p class="benefits-lead">Here are just a few of them:</p>
        <ul class="benefit-list">
          <li>Lorem ipsum dolor sit amet, consectetur adipiscing elit.</li>
          <li>Vestibulum ante ipsum primis in faucibus orci luctus et ultrices posuere cubilia.</li>
          <li>Nunc ac massa massa. In et risus leo, commodo laoreet risus.</li>
          <li>Pellentesque cursus mattis eros vel lobortis. Etiam in purus odio, in malesuada.</li>
          <li>Lorem ipsum dolor sit amet, consectetur adipiscing elit</li>
          <li>Vestibulum ante ipsum primis in faucibus orci luctus et ultrices posuere cubilia.</li>
          <li>Nunc ac massa massa. In et risus leo, commodo laoreet risus.</li>
          <li>Suspendisse facilisis porttitor tellus, sed eleifend tellus semper vitae.</li>
          <li>Vestibulum ante ipsum primis in faucibus orci luctus et ultrices posuere cubilia Curae; Nunc ac massa massa. In et risus leo, commodo laoreet risus.</li>
          <li>Suspendisse facilisis porttitor tellus, sed eleifend tellus semper vitae.</li>
          <li>Vestibulum ante ipsum primis in faucibus orci luctus et ultrices posuere cubilia Curae; Nunc ac massa massa. In et risus leo, commodo laoreet risus.</li>
          <li>Pellentesque cursus mattis eros vel lobortis. Etiam in purus odio, in malesuada mauris. Mauris mattis magna eget magna volutpat eu pulvinar metus tristique.</li>
          <li>Suspendisse facilisis porttitor tellus, sed eleifend tellus semper vitae.</li>
        </ul>
      </div>

      <div class="benefits-band">
        <h2 class="band-title">What are the Benefits?</h2>
        <p class="band-tagline"><span>Owning a stateroom will be one of the</span><span>greatest decisions you ever make</span></p>
      </div>

      <div class="accent-sky"></div>
      <div class="photo-deck" role="img" aria-label="Photograph: two wooden deck chairs and a small table on a ship's teak deck overlooking the sea"></div>
    </section>
  </div>

  <div class="fold"></div>
  <span class="folio folio-left">04</span>
  <span class="folio folio-right">05</span>
</body>
</html>
```